The Tress Arbor needs Business Cards

The Tress Arbor is a premier provider of natural hair extensions and wigs. We're looking for a double sided business card that complements our logo and is consistent with the style, look and feel of our logo/image.

```html
<!DOCTYPE html>
<html lang="en">
<head>
<meta charset="utf-8">
<title>The Tress Arbor — Business Cards</title>
<link href="https://fonts.googleapis.com/css2?family=Montserrat:wght@500;600&family=Tinos:wght@400&display=swap" rel="stylesheet">
<style>
  :root {
    --stage: #1c1c1e;
    --card: #ffffff;
    --ink: #1b1b1b;
    --gold: #c29a3e;
    --navy: #2f3f6e;
    --rule: #222222;
  }
  * { margin: 0; padding: 0; box-sizing: border-box; }
  html, body {
    width: 1200px; height: 800px; overflow: hidden;
    background: var(--stage);
  }
  .stage {
    width: 1200px; height: 800px;
    display: flex; align-items: center; justify-content: center; gap: 60px;
  }
  .card {
    position: relative;
    width: 520px; height: 300px;
    background: var(--card);
    border-radius: 26px;
    box-shadow: 0 10px 30px rgba(0,0,0,.45);
    overflow: hidden;
  }
  .brand { text-align: center; }
  .brand-name {
    font-family: "Montserrat", sans-serif;
    font-weight: 600;
    color: var(--ink);
    letter-spacing: .5px;
    display: inline-flex; align-items: center; gap: 10px;
    white-space: nowrap;
  }
  .brand-dot {
    width: 14px; height: 14px; border-radius: 50%;
    background: var(--gold); display: inline-block;
  }
  .brand-tagline {
    font-family: "Montserrat", sans-serif;
    font-weight: 500;
    color: var(--ink);
  }

  /* Front */
  .card-front { display: flex; align-items: center; justify-content: center; }
  .card-front .brand-name { font-size: 40px; }
  .card-front .brand-tagline { font-size: 15px; letter-spacing: 4px; margin-top: 6px; }

  /* Back */
  .card-back .brand { position: absolute; top: 34px; left: 0; right: 0; }
  .card-back .brand-name { font-size: 26px; gap: 8px; }
  .card-back .brand-dot { width: 10px; height: 10px; }
  .card-back .brand-tagline { font-size: 10px; letter-spacing: 2.6px; margin-top: 3px; }
  .rule-top {
    position: absolute; top: 98px; right: 40px; width: 200px;
    border-top: 2px solid var(--rule);
  }
  .rule-mid {
    position: absolute; top: 150px; left: 40px; width: 190px;
    border-top: 2px solid var(--rule);
  }
  .person {
    position: absolute; left: 40px; top: 192px;
    font-family: "Tinos", serif; color: var(--ink);
    white-space: nowrap;
  }
  .person-name { font-size: 23px; }
  .person-title { font-size: 18px; margin-top: 2px; }
  .contact-list {
    position: absolute; left: 258px; top: 130px;
    list-style: none;
    font-family: "Tinos", serif; font-size: 13px; color: var(--ink);
    white-space: nowrap;
  }
  .contact-list li {
    display: flex; align-items: center; gap: 9px; height: 26px;
  }
  .contact-icon { width: 16px; height: 16px; flex: none; }
</style>
</head>
<body>
<main class="stage">

  <section class="card card-front" aria-label="Business card front">
    <div class="brand">
      <div class="brand-name"><span class="brand-dot"></span>The Tress Arbor</div>
      <div class="brand-tagline">Vigin Hair Extensions</div>
    </div>
  </section>

  <section class="card card-back" aria-label="Business card back">
    <div class="brand">
      <div class="brand-name"><span class="brand-dot"></span>The Tress Arbor</div>
      <div class="brand-tagline">Vigin Hair Extensions</div>
    </div>
    <div class="rule-top"></div>
    <div class="rule-mid"></div>

    <div class="person">
      <div class="person-name">Daniel R. Whitcombe</div>
      <div class="person-title">Director</div>
    </div>

    <ul class="contact-list">
      <li>
        <svg class="contact-icon" viewBox="0 0 16 16" aria-hidden="true">
          <rect width="16" height="16" rx="3" fill="var(--navy)"/>
          <path d="M5 3.5c.6 0 1.2 1.6 1.2 2.1 0 .6-.8.8-.7 1.4.3 1 1.3 2 2.3 2.3.6.1.8-.7 1.4-.7.5 0 2.1.6 2.1 1.2 0 .9-1 1.700-1.900 1.7C6.6 11.5 4.5 9.4 4.5 6.6c0-.9.5-3.1.5-3.1z" fill="#fff"/>
        </svg>
        325-555-0142
      </li>
      <li>
        <svg class="contact-icon" viewBox="0 0 16 16" aria-hidden="true">
          <rect width="16" height="16" rx="3" fill="var(--navy)"/>
          <rect x="3" y="5" width="10" height="7" fill="none" stroke="#fff" stroke-width="1.2"/>
          <path d="M3 5l5 4 5-4" fill="none" stroke="#fff" stroke-width="1.2"/>
        </svg>
        DanielRWhitcombe@tressmail.us
      </li>
      <li>
        <svg class="contact-icon" viewBox="0 0 16 16" aria-hidden="true">
          <path d="M8 2 1.5 8H4v6h3v-4h2v4h3V8h2.5z" fill="var(--navy)"/>
        </svg>
        2718 Cedar Hollow, TX 76904
      </li>
      <li>
        <svg class="contact-icon" viewBox="0 0 16 16" aria-hidden="true">
          <circle cx="8" cy="8" r="7.5" fill="var(--navy)"/>
          <ellipse cx="8" cy="8" rx="3" ry="6" fill="none" stroke="#fff" stroke-width="1"/>
          <path d="M2 8h12M3 5h10M3 11h10" stroke="#fff" stroke-width="1"/>
        </svg>
        www.tressarbor.com
      </li>
    </ul>
  </section>

</main>
</body>
</html>
```